"Brightwall Sound Living Residences" need a busines Card Design got Builder

We need a business card design for a company based in Milford, Michigancalled Brightwall Sound Living Residences - has been recognized as a premier custom home builder. Distinguished by outstanding craftmanship and timeless beauty. Our custom home can be found in the most prestigious communities in Michigan. The homes are built with ICF (insulated concrete homes) which is green, allergy free, fire free, mold free and quitter. Our slogan "building one dream at a Time" and also we are ICF distributor for the state of Michigan

Target Market(s)

Anyone who is making over $100,000 a year and who wants to have totally custom built home. Ages from 29 up to 60 years old

Industry/Entity Type

Concrete

Contact Information for Business Card

we want to use - green, black, gray or blue colors - we want to look different with our business cards, because we built homes only with ICF, green, healthier and highly energy efficient homes.

Requirements
Must have
• I have logo that I attached and we have been using the logo (the only green home)
Nice to have
• should look quality business card,

Files

```html
<!DOCTYPE html>
<html lang="en">
<head>
<meta charset="utf-8">
<title>Brightwall Sound Living Residences – Business Card</title>
<link rel="stylesheet" href="https://fonts.googleapis.com/css2?family=Michroma&family=Open+Sans:wght@400;700&display=swap">
<style>
  :root {
    --backdrop: #e8e6e3;
    --card-black: #1f1f1f;
    --card-back: #202020;
    --emboss-gray: #3a3a3a;
    --emboss-text: #121212;
    --brand-green: #9dc43c;
    --light-green: #c9e27f;
    --white: #ffffff;
  }
  * { margin: 0; padding: 0; box-sizing: border-box; }
  html, body {
    width: 1200px;
    height: 1000px;
    overflow: hidden;
    background: var(--backdrop);
  }
  .canvas {
    position: relative;
    width: 1200px;
    height: 1000px;
  }
  .card {
    position: absolute;
    left: 250px;
    width: 697px;
    height: 416px;
    border-radius: 22px;
    overflow: hidden;
    box-shadow: 0 6px 18px rgba(0,0,0,0.25);
  }
  .card-back { top: 63px; background: var(--card-back); }
  .card-front { top: 522px; background: var(--card-black); }

  .card-shapes {
    position: absolute;
    inset: 0;
    width: 697px;
    height: 416px;
  }

  .brand-mark {
    position: absolute;
    border-radius: 50%;
  }
  .card-back .brand-mark {
    left: 80px; top: 127px;
    width: 150px; height: 150px;
    background: var(--emboss-gray);
  }
  .card-front .brand-mark {
    left: 102px; top: 70px;
    width: 138px; height: 138px;
    background: var(--brand-green);
  }

  .brand-name {
    position: absolute;
    font-family: "Michroma", sans-serif;
    font-weight: 400;
    text-transform: uppercase;
    line-height: 1.2;
    letter-spacing: 0.5px;
  }
  .card-back .brand-name {
    left: 250px; top: 186px;
    font-size: 20px;
    color: var(--emboss-text);
  }
  .card-front .brand-name {
    left: 257px; top: 104px;
    font-size: 19px;
    color: var(--white);
  }

  .tagline {
    position: absolute;
    left: 0; right: 0; top: 239px;
    text-align: center;
    padding-right: 50px;
    font-family: "Open Sans", sans-serif;
    font-weight: 700;
    font-size: 17px;
    color: var(--white);
    letter-spacing: 0.2px;
  }

  .address {
    position: absolute;
    right: 369px; top: 313px;
    text-align: right;
    font-family: "Open Sans", sans-serif;
    font-size: 18px;
    line-height: 27px;
    color: var(--white);
  }
  .contact-divider {
    position: absolute;
    left: 346px; top: 302px;
    width: 2px; height: 68px;
    background: var(--brand-green);
  }
  .contact-list {
    position: absolute;
    left: 362px; top: 298px;
    list-style: none;
    font-family: "Open Sans", sans-serif;
    font-size: 17.5px;
    line-height: 22.5px;
    color: var(--white);
  }
  .contact-list li {
    display: flex;
    align-items: center;
    gap: 8px;
  }
  .contact-icon {
    width: 14px; height: 14px;
    fill: var(--white);
    flex: none;
  }
</style>
</head>
<body>
<main class="canvas">

  <section class="card card-back" aria-label="Card back">
    <span class="brand-mark" aria-hidden="true"></span>
    <p class="brand-name">Brightwall Sound<br>Living Residences</p>
  </section>

  <section class="card card-front" aria-label="Card front">
    <svg class="card-shapes" viewBox="0 0 697 416" aria-hidden="true">
      <path d="M488 0 H697 V200 C672 95 592 22 488 0 Z" fill="var(--brand-green)"/>
      <path d="M522 14 C612 40 672 100 688 176" fill="none" stroke="var(--light-green)" stroke-width="3"/>
      <path d="M0 222 C22 318 108 388 212 416 H0 Z" fill="var(--brand-green)"/>
      <path d="M10 240 C40 326 106 378 178 404" fill="none" stroke="var(--light-green)" stroke-width="3"/>
    </svg>

    <span class="brand-mark" aria-hidden="true"></span>
    <p class="brand-name">Brightwall Sound<br>Living Residences</p>

    <p class="tagline">"BUILDING ONE DREAM AT A TIME"</p>

    <address class="address" style="font-style:normal">
      22 Harrow Crest Drive<br>Kelsey VIC 3760
    </address>

    <span class="contact-divider" aria-hidden="true"></span>

    <ul class="contact-list">
      <li>
        <svg class="contact-icon" viewBox="0 0 24 24" aria-hidden="true"><path d="M6.6 10.8a15.1 15.1 0 0 0 6.6 6.6l2.2-2.2a1 1 0 0 1 1-.25 11.4 11.4 0 0 0 3.6.57 1 1 0 0 1 1 1V20a1 1 0 0 1-1 1A17 17 0 0 1 3 4a1 1 0 0 1 1-1h3.5a1 1 0 0 1 1 1c0 1.25.2 2.45.57 3.57a1 1 0 0 1-.25 1z"/></svg>
        <span>+ 555 014 2280</span>
      </li>
      <li>
        <svg class="contact-icon" viewBox="0 0 24 24" aria-hidden="true"><path d="M2 5h20v14H2z M3.5 6.5 12 13l8.5-6.5" fill="var(--white)" stroke="var(--card-black)" stroke-width="1.6"/></svg>
        <span>info@brightwallsound.com</span>
      </li>
      <li>
        <svg class="contact-icon" viewBox="0 0 24 24" aria-hidden="true"><circle cx="12" cy="12" r="10"/><path d="M2 12h20M12 2c3 3 3 17 0 20M12 2c-3 3-3 17 0 20M4 7h16M4 17h16" fill="none" stroke="var(--card-black)" stroke-width="1.4"/></svg>
        <span>www.brightwallsound.com</span>
      </li>
    </ul>
  </section>

</main>
</body>
</html>
```